Web Design Project and logo

We need a new web design and logo for www.kq7ventra.com

It is a mobile app development company. Site needs to look very cool/trendy as does the new logo.

Looking for the design (uncoded) and the logo file that my developers can then use to build out the site.

An example of a nice competitor site is www.plumwirestudio.com

We want something that looks fresh, clean and hip.

Also development of business cards.

Target Market(s)

Small to mid sized companies

Industry/Entity Type

Business

Requirements
Must have
• Ability to request a quote
Should look very trendy like www.plumwirestudio.com as an example of a competitor site

```html
<!DOCTYPE html>
<html lang="en">
<head>
<meta charset="utf-8">
<title>KQ7 Ventra – Home Page Design</title>
<link rel="stylesheet" href="https://fonts.googleapis.com/css2?family=Open+Sans:wght@300;400;600;700&display=swap">
<style>
:root{
  --coral:#f04a3a;
  --ink:#3a3a3a;
  --mid:#7b7b7b;
  --soft:#a8a8a8;
  --board:#e9e9e9;
  --panel:#f3f3f3;
  --white:#ffffff;
  --dark:#141414;
  --teal-a:#0d2f3a;
  --teal-b:#3f8ea0;
  --teal-c:#b9e3ea;
}
*{margin:0;padding:0;box-sizing:border-box}
html,body{width:1200px;height:1000px;overflow:hidden}
body{
  font-family:"Open Sans",Arial,sans-serif;
  color:var(--ink);
  background:radial-gradient(ellipse at 70% 20%,#f7f7f7 0%,#ececec 55%,#e3e3e3 100%);
  position:relative;
}
.brand-mark{position:absolute;left:44px;top:168px;width:300px}
.brand-mark__name{font-size:70px;font-weight:700;letter-spacing:1px;color:var(--coral);line-height:1}
.brand-mark__tag{font-size:25px;font-weight:400;letter-spacing:11px;color:var(--ink);margin-top:34px}

.site{position:absolute;left:385px;top:14px;width:425px;height:971px;background:var(--white);overflow:hidden;box-shadow:0 0 12px rgba(0,0,0,.06)}
.abs{position:absolute}

/* nav */
.nav{left:0;top:0;width:425px;height:24px;background:var(--white);font-size:4.6px;color:var(--mid)}
.nav__logo{left:10px;top:5px;font-size:10px;font-weight:700;color:var(--coral);line-height:1}
.nav__logo small{display:block;font-size:3px;letter-spacing:1.2px;color:var(--ink);font-weight:400;margin-top:1px}
.nav__links{left:78px;top:0;display:flex;height:24px;align-items:center}
.nav__links span{padding:0 7px;height:24px;line-height:24px;border-left:1px solid #eee}
.nav__links .is-active{color:var(--ink)}
.nav__call{left:254px;top:9px}
.nav__lang{left:324px;top:9px}
.nav__btn{left:370px;top:7px;width:43px;height:10px;background:#d6d6d6;border-radius:2px;color:var(--white);text-align:center;line-height:10px;font-size:4px}

/* hero */
.hero{left:0;top:24px;width:425px;height:246px}
.hero__photo{left:0;top:0;width:425px;height:246px;background:
  radial-gradient(ellipse at 78% 40%,var(--teal-c) 0%,rgba(185,227,234,0) 45%),
  radial-gradient(ellipse at 30% 55%,var(--teal-b) 0%,rgba(63,142,160,0) 60%),
  linear-gradient(160deg,#1c4a57 0%,var(--teal-a) 100%)}
.hero__title{left:37px;top:35px;color:var(--white);font-size:17px;font-weight:300;line-height:17px;letter-spacing:.3px}
.hero__lead{left:38px;top:80px;color:var(--white);font-size:4.6px}
.field{height:13px;background:var(--white);border-radius:2px;font-size:4.8px;color:#c2c2c2;padding-left:4px;line-height:13px}
.hero__submit{left:38px;top:166px;width:146px;height:20px;background:var(--coral);color:var(--white);font-size:5px;font-weight:600;text-align:center;line-height:20px;border-radius:2px}
.feature{top:219px;width:136px;height:36px;background:rgba(10,20,24,.82);color:var(--white);padding:6px 6px 0 30px;font-size:3.9px;line-height:5px}
.feature b{display:block;font-weight:600;font-size:4.4px;margin-bottom:1px}
.feature svg{position:absolute;left:9px;top:9px}

/* intro band */
.intro{left:0;top:270px;width:425px;height:45px;background:var(--panel);text-align:center}
.intro h2{font-weight:400;font-size:8.4px;color:var(--ink);margin-top:13px;line-height:9px}
.intro h2 span{display:block;color:var(--coral);font-weight:600}

/* process */
.process{left:0;top:315px;width:425px;height:122px;display:flex;background:#fbfbfb}
.step{width:85px;height:122px;border-right:1px solid #ececec;padding:0 5px;text-align:center;color:var(--mid);position:relative}
.step svg{margin-top:22px}
.step h3{font-size:5px;font-weight:400;line-height:7px;height:16px;margin-top:8px}
.step p{text-align:left;font-size:4.6px;line-height:7px;margin-top:5px}
.step em{display:block;text-align:left;font-size:4.4px;margin-top:6px}
.step--active{background:var(--coral);color:var(--white)}
.step--active::before{content:"";position:absolute;left:37px;top:-5px;border:6px solid transparent;border-top:6px solid var(--white);border-bottom:0}
.step--active p{font-weight:600}

/* about */
.about{left:0;top:437px;width:425px;height:141px;background:var(--white)}
.about h3{font-size:8.5px;font-weight:400;color:var(--ink)}
.about p{font-size:4.5px;line-height:6.8px;color:var(--mid)}
.about .more{font-size:4.4px;color:var(--mid)}
.about__video{left:157px;top:47px;width:127px;height:71px;background:linear-gradient(120deg,#1a1f2a 0%,#1f5f8f 55%,#4fb0d9 100%)}
.about__video svg{position:absolute;left:48px;top:20px}
.avatar{top:59px;width:28px;height:29px;background:#9e9e9e}
.avatar--hi{background:var(--coral)}

/* facts */
.facts-band{left:0;top:578px;width:425px;height:44px;background:var(--panel);text-align:center}
.facts-band h2{font-size:8px;font-weight:400;margin-top:14px;line-height:9px}
.facts-band h2 span{display:block;color:var(--coral);font-weight:600;font-size:7.4px}
.facts{left:0;top:622px;width:425px;height:196px;background:#fafafa}
.facts__phone{left:44px;top:8px;width:90px;height:176px;border-radius:14px;background:linear-gradient(180deg,#3a3a3a,#0e0e0e)}
.facts__screen{left:53px;top:38px;width:72px;height:112px;background:linear-gradient(180deg,#3c4a58 0%,#6b7a87 70%,#e8eef5 100%)}
.facts__laptop-lid{left:290px;top:27px;width:140px;height:135px;background:var(--dark);border-radius:6px 0 0 0}
.facts__laptop-screen{left:298px;top:37px;width:135px;height:120px;background:linear-gradient(180deg,#202020,#161616)}
.facts__laptop-base{left:266px;top:162px;width:160px;height:8px;background:linear-gradient(180deg,#dcdcdc,#9a9a9a);border-radius:0 0 0 8px}
.stats{left:150px;top:24px;width:125px;text-align:center;color:var(--ink)}
.stat{font-size:8px;line-height:9px;font-weight:400}
.stat b{display:block;font-weight:700}
.stat--red{color:var(--coral)}
.stat--red span{color:var(--ink);font-weight:400}
.op{font-size:12px;color:var(--soft);line-height:12px;margin:8px 0}

/* tech strip */
.tech{left:0;top:818px;width:425px;height:52px;background:var(--white);display:flex;align-items:center;justify-content:space-between;padding:0 12px;color:#9b9b9b}
.tech span{font-size:10px;font-weight:700}
.tech .arrow{font-size:9px;font-weight:400}

/* footer */
.footer{left:0;top:870px;width:425px;height:84px;background:var(--panel);font-size:4.4px;color:var(--mid);line-height:7.6px}
.footer h4{font-size:4.4px;font-weight:400;color:var(--mid);margin-bottom:4px}
.footer__logo{font-size:10px;font-weight:700;color:var(--coral);line-height:10px}
.footer__menu b{color:var(--ink);font-weight:600}
.footer__newsletter{width:96px;height:12px;background:var(--white);line-height:12px;padding-left:4px;color:#999}
.dot{display:inline-block;width:4px;height:4px;border-radius:50%;background:#9b9b9b;margin-right:4px}
.legal{left:0;top:954px;width:425px;height:17px;background:#0d0d0d;color:#cfcfcf;font-size:3.8px;text-align:center;line-height:17px}
</style>
</head>
<body>

<div class="brand-mark">
  <div class="brand-mark__name">KQ7 VENTRA</div>
</div>

<main class="site">
  <header class="abs nav">
    <div class="abs nav__logo">KQ7<small>VENTRA</small></div>
    <nav class="abs nav__links">
      <span class="is-active">HOME</span><span>OUR SERVICES</span><span>LATEST NEWS</span><span>CONTACT</span>
    </nav>
    <div class="abs nav__call">CALL US ON: +00 000 0000</div>
    <div class="abs nav__lang">ENGLISH ⌄</div>
    <div class="abs nav__btn">I NEED APP NOW!</div>
  </header>

  <section class="abs hero">
    <div class="abs hero__photo" role="img" aria-label="Photo of a hand touching glowing app icons on a blue screen"></div>
    <h1 class="abs hero__title">BEGINS WITH THE<br>NO1 APP PROVIDER</h1>
    <p class="abs hero__lead">To start your experience fill the form below</p>
    <div class="abs field" style="left:38px;top:94px;width:146px">Full Name</div>
    <div class="abs field" style="left:38px;top:113px;width:70px">Company</div>
    <div class="abs field" style="left:114px;top:113px;width:70px">Country</div>
    <div class="abs field" style="left:38px;top:132px;width:70px">Email address</div>
    <div class="abs field" style="left:114px;top:132px;width:70px">Phone</div>
    <div class="abs hero__submit">CONTACT US NOW!</div>

    <div class="abs feature" style="left:0">
      <svg width="14" height="16" viewBox="0 0 14 16"><rect x="1" y="1" width="8" height="14" rx="1" fill="none" stroke="#fff" stroke-width="1.2"/><rect x="7" y="5" width="6" height="10" rx="1" fill="none" stroke="#fff" stroke-width="1.2"/></svg>
      <b>MOBILE SERVICES</b>Our comprehensive range of consulting services takes you from idea through development.
    </div>
    <div class="abs feature" style="left:145px">
      <svg width="14" height="14" viewBox="0 0 14 14"><path d="M7 13 L1.5 7 A3.2 3.2 0 0 1 7 3 A3.2 3.2 0 0 1 12.5 7 Z" fill="#fff"/></svg>
      <b>QUALITY THROUGH EXPERIENCE</b>Our team of engineers knows what it takes to serve more than 1,000,000 happy customers.
    </div>
    <div class="abs feature" style="left:289px">
      <svg width="14" height="14" viewBox="0 0 14 14"><circle cx="7" cy="7" r="5" fill="none" stroke="#fff" stroke-width="1.2"/><path d="M7 0v14M0 7h14" stroke="#fff" stroke-width="1.2"/></svg>
      <b>I WANT YOU!</b>KQ7 Ventra is always looking for talented developers. If you have what it takes, contact us!
    </div>
  </section>

  <section class="abs intro"><h2>UNIQUE EXPERIENCES FOR<span>MOBILE</span></h2></section>

  <section class="abs process">
    <article class="step step--active">
      <svg width="14" height="18" viewBox="0 0 14 18"><path d="M7 0 C7 0 1 8 1 11 A6 6 0 0 0 13 11 C13 8 7 0 7 0Z" fill="#fff"/></svg>
      <h3>NEEDS</h3>
      <p>Lorem Ipsum is simply dummy text of the printing and typesetting industry.</p>
      <em>Read more</em>
    </article>
    <article class="step">
      <svg width="14" height="18" viewBox="0 0 14 18"><path d="M7 0 C11 3 11 9 10 13 H4 C3 9 3 3 7 0Z" fill="#6b6b6b"/><path d="M4 10 L1 15 H4ZM10 10 L13 15 H10Z" fill="#6b6b6b"/><circle cx="7" cy="6" r="1.6" fill="#fbfbfb"/></svg>
      <h3>PLANNING AND<br>RAPID PROTOTYPING</h3>
      <p>Lorem Ipsum is simply dummy text of the printing and typesetting industry.</p>
      <em>Read more</em>
    </article>
    <article class="step">
      <svg width="12" height="18" viewBox="0 0 12 18"><rect x="0.5" y="0.5" width="11" height="17" rx="2" fill="#6b6b6b"/><rect x="2" y="3" width="8" height="11" fill="#fbfbfb"/><circle cx="6" cy="8.5" r="2" fill="#6b6b6b"/></svg>
      <h3>CODING AND<br>TESTING</h3>
      <p>Lorem Ipsum is simply dummy text of the printing and typesetting industry.</p>
      <em>Read more</em>
    </article>
    <article class="step">
      <svg width="22" height="16" viewBox="0 0 22 16"><path d="M5 15 A4.5 4.5 0 0 1 5 6 A6 6 0 0 1 16.5 5 A5 5 0 0 1 17 15Z" fill="#6b6b6b"/></svg>
      <h3>COMPLETION AND<br>MARKET INTRODUCTION</h3>
      <p>Lorem Ipsum is simply dummy text of the printing and typesetting industry.</p>
      <em>Read more</em>
    </article>
    <article class="step" style="border-right:0">
      <svg width="18" height="18" viewBox="0 0 18 18"><rect x="1" y="12" width="3" height="6" fill="#6b6b6b"/><rect x="5.5" y="9" width="3" height="9" fill="#6b6b6b"/><rect x="10" y="6" width="3" height="12" fill="#6b6b6b"/><rect x="14.5" y="2" width="3" height="16" fill="#6b6b6b"/></svg>
      <h3>ANALYSIS &amp;<br>IMPROVEMENTS</h3>
      <p>Lorem Ipsum is simply dummy text of the printing and typesetting industry.</p>
      <em>Read more</em>
    </article>
  </section>

  <section class="abs about">
    <h3 class="abs" style="left:12px;top:44px">ABOUT US</h3>
    <p class="abs" style="left:12px;top:57px;width:130px">KQ7 Ventra is a specialty mobile solutions provider with expertise across all the major mobile platforms. We have a track record with several apps reaching the top 10 most downloaded lists. Deep knowledge of how to create and manage robust and intuitive apps has been acquired by the experience rendered from serving 1,000,000 customers.</p>
    <span class="abs more" style="left:12px;top:116px">Read more</span>
    <div class="abs about__video" role="img" aria-label="Video still of a businessman holding a phone with app icons">
      <svg width="32" height="32" viewBox="0 0 32 32"><circle cx="16" cy="16" r="14" fill="none" stroke="#fff" stroke-width="2.5"/><path d="M12 9 L23 16 L12 23Z" fill="#fff"/></svg>
    </div>
    <h3 class="abs" style="left:307px;top:44px">CUSTOMERS ARE SAYING</h3>
    <div class="abs avatar avatar--hi" style="left:307px" role="img" aria-label="Customer portrait"></div>
    <div class="abs avatar" style="left:346px" role="img" aria-label="Customer portrait"></div>
    <div class="abs avatar" style="left:384px" role="img" aria-label="Customer portrait"></div>
    <p class="abs" style="left:307px;top:94px;width:108px">Lorem Ipsum is simply dummy text of the printing and typesetting industry.</p>
    <span class="abs more" style="left:307px;top:116px">Read more</span>
  </section>

  <section class="abs facts-band"><h2>A FACT WORTH A THOUSAND WORDS,<span>OUR CLIENTS LOVE US AND WHY THEY KEEP COMING BACK</span></h2></section>

  <section class="abs facts">
    <div class="abs facts__phone" role="img" aria-label="Smartphone showing a word game app"></div>
    <div class="abs facts__screen" role="img" aria-label="Game board with coloured tiles and score list"></div>
    <div class="stats abs">
      <div class="stat"><b>1,000,000</b>HAPPY CUSTOMERS</div>
      <div class="op">+</div>
      <div class="stat"><b>X YEARS</b>OFF EXPERIENCE</div>
      <div class="op">+</div>
      <div class="stat"><b>FAMOUS</b>APPLICATIONS</div>
      <div class="op">=</div>
      <div class="stat stat--red"><b>100%</b><span>SATISFACTION</span></div>
    </div>
    <div class="abs facts__laptop-lid"></div>
    <div class="abs facts__laptop-screen" role="img" aria-label="Laptop screen showing code in an editor"></div>
    <div class="abs facts__laptop-base"></div>
  </section>

  <section class="abs tech">
    <span class="arrow">‹</span>
    <span>Qelix</span><span>Javelo</span><span>Hypermark</span><span>Tabulo</span><span>Appfield</span><span>Appfield</span>
    <span class="arrow">›</span>
  </section>

  <footer class="abs footer">
    <div class="abs" style="left:12px;top:16px;width:112px">
      <div class="footer__logo">KQ7</div>
      <div style="font-size:3px;letter-spacing:1px;line-height:4px;margin-bottom:4px">VENTRA</div>
      KQ7 Ventra is a specialty mobile solutions provider with expertise across all the major mobile platforms.
    </div>
    <div class="abs footer__menu" style="left:138px;top:12px">
      <h4>MENU</h4><b>HOME</b><br>OUR SERVICES<br>LATEST NEWS<br>CONTACT
    </div>
    <div class="abs" style="left:197px;top:12px;width:100px">
      <h4 style="margin-left:12px">CONTACT US</h4>
      <div style="padding-left:12px;line-height:6px">ADDRESS: LANTERN YARD 4, ORCHARD LANE, MILLBROOK, WESTSHIRE WS4 8QT UNITED KINGDOM</div>
      <div style="padding-left:12px;margin-top:3px">PHONE: +00 000 0000</div>
      <div style="padding-left:12px">EMAIL: MAIL@EXAMPLE.COM</div>
    </div>
    <div class="abs" style="left:318px;top:12px">
      <h4>FOLLOW US</h4>
      <div><span class="dot"></span><span class="dot"></span><span class="dot"></span><span class="dot"></span></div>
      <div style="margin-top:2px">SIGN UP FOR OUR NEWSLETTER:</div>
      <div class="footer__newsletter" style="margin-top:2px">Enter your email address here...</div>
    </div>
  </footer>
  <div class="abs legal">COPYRIGHT KQ7 VENTRA 2013. ALL RIGHTS RESERVED.</div>
</main>

</body>
</html>
```